Flyer für einen Sanitär Heizungs Betrieb
Zielgruppe
Sanitär Heizungs Betrieb der den Fokus verstärkt auf den Service an Heizungsanlagen setzten will.
Der Flyer soll sowohl an Privathaushalte als auch an Hausverwaltungen gehen.
Er soll unsere Leistungen aufzeigen und einen guten ersten Eindruck vermitteln.
Aufgabenstellung
Anbei sende ich Themen die als Leistung aufgeführt werden, sowie Strichwort für einen Werbetext (kann gerne generiert werden ansonsten kommt er noch zum texter)

```html
<!DOCTYPE html>
<html lang="de">
<head>
<meta charset="utf-8">
<title>Flyer Heizungsservice</title>
<link href="https://fonts.googleapis.com/css2?family=Open+Sans:wght@400;600;700;800&display=swap" rel="stylesheet">
<style>
  :root {
    --bg: #dedede;
    --paper: #f7f7f7;
    --paper-shade: #efefef;
    --ink: #2a2a2a;
    --ink-soft: #5a5a5a;
    --blue: #2f86c8;
    --red: #e03a3e;
    --yellow: #d8b21a;
    --blue-icon: #2a7fc0;
    --grey-icon: #8c8c8c;
    --fold: #d6d6d6;
  }
  * { box-sizing: border-box; margin: 0; padding: 0; }
  html, body { width: 1200px; height: 784px; overflow: hidden; }
  body { background: var(--bg); font-family: "Open Sans", Arial, sans-serif; color: var(--ink); position: relative; }

  .flyer {
    position: absolute; left: 40px; top: 152px; width: 1120px; height: 480px;
    display: flex; box-shadow: 0 18px 40px rgba(0,0,0,.15);
  }
  .panel { position: relative; width: 560px; height: 480px; background: var(--paper); overflow: hidden; }
  .panel--inside-left { background: linear-gradient(90deg, var(--paper) 80%, var(--paper-shade)); }
  .panel--inside-right { border-left: 1px solid var(--fold); }

  .intro { position: absolute; left: 30px; top: 150px; width: 195px; font-size: 12px; font-weight: 700; line-height: 1.35; }
  .about { position: absolute; left: 30px; top: 300px; width: 195px; font-size: 10.5px; line-height: 1.45; color: var(--ink-soft); }
  .approach { position: absolute; left: 240px; top: 34px; width: 150px; font-size: 10px; line-height: 1.45; color: var(--ink-soft); }

  .services { position: absolute; left: 240px; top: 196px; width: 150px; }
  .services__title { font-size: 11px; font-weight: 800; letter-spacing: .02em; margin-bottom: 6px; }
  .services__list { list-style: none; font-size: 11px; font-weight: 700; line-height: 1.85; }
  .services__list li::before { content: "• "; }

  .service-icons { position: absolute; left: 398px; top: 188px; display: flex; flex-direction: column; gap: 9px; }
  .service-icons svg { width: 30px; height: 30px; display: block; }

  .photo { position: absolute; }
  .photo--client { left: 400px; top: 18px; width: 160px; height: 156px; background: linear-gradient(135deg, #e9eef0 0%, #c9d6dc 45%, #6f95ad 75%, #cfd9de 100%); }
  .photo--boiler-room { left: 38px; top: 140px; width: 220px; height: 180px; background: linear-gradient(160deg, #f2f2f2 0%, #cfd2d5 40%, #b7bcc1 60%, #ececec 100%); }

  .process { position: absolute; left: 440px; top: 192px; width: 116px; height: 170px; font-size: 8.5px; line-height: 1.3; color: var(--ink-soft); }
  .process__step { position: absolute; }
  .process__step strong { display: block; color: var(--ink); font-weight: 700; }
  .process__step--1 { left: 0; top: 34px; width: 58px; }
  .process__step--2 { left: 60px; top: 0; width: 56px; }
  .process__step--3 { left: 14px; top: 118px; width: 96px; }
  .process__arrows { position: absolute; left: 0; top: 0; width: 116px; height: 170px; }

  .claim { position: absolute; left: 30px; top: 400px; font-size: 16px; color: var(--blue); line-height: 1.3; }
  .claim strong { display: block; font-weight: 800; }

  .staff-title { position: absolute; left: 28px; top: 58px; font-size: 15px; color: var(--blue); line-height: 1.25; }
  .staff-title strong { display: block; font-weight: 700; }

  .tasks { position: absolute; font-size: 9.5px; line-height: 1.35; color: var(--ink-soft); }
  .tasks--main { left: 280px; top: 40px; width: 130px; }
  .tasks--more { left: 420px; top: 14px; width: 130px; }
  .tasks dt { font-weight: 700; color: var(--ink); margin-top: 7px; font-size: 10px; }
  .tasks dt:first-child { margin-top: 0; }
  .tasks dd { margin: 0; }

  .benefits { position: absolute; left: 300px; top: 300px; width: 260px; height: 86px; background: var(--red); color: #fff; padding: 14px 18px; list-style: none; font-size: 12px; font-weight: 600; line-height: 1.45; letter-spacing: .02em; }
  .benefits li::before { content: "• "; }
</style>
</head>
<body>
  <main class="flyer">
    <section class="panel panel--inside-left">
      <p class="intro">Wenn Sie nach einem erfahrenen und zuverlässigen Lindholm Wärmetechnik Service mit Kompetenz in Heizung, Badsanierung, Brennstoff&shy;zellenheizung und Wärmepumpen suchen, sind Sie bei uns genau richtig!</p>
      <p class="approach">Wir beraten Sie sehr gerne und nehmen uns für Sie Zeit. Unser Anspruch ist es unsere Kunden fachlich und projektbezogen zu beraten und unsere technische Arbeit zuverlässig durchzuführen.</p>
      <p class="about">Wir als Lindholm Wärmetechnik Unternehmen legen sehr viel Wert auf Kundenzufriedenheit und professionelle Ausführungsqualität.</p>

      <div class="services">
        <h2 class="services__title">UNSERE LEISTUNGEN</h2>
        <ul class="services__list">
          <li>Heizung</li>
          <li>Brennstoffzellenheizung</li>
          <li>Badsanierung</li>
          <li>Wärmepumpe</li>
        </ul>
      </div>

      <div class="service-icons">
        <svg viewBox="0 0 32 32" aria-label="Heizung"><circle cx="16" cy="16" r="16" fill="var(--red)"/><g stroke="#fff" stroke-width="1.6"><path d="M9 11v11M12 11v11M15 11v11M18 11v11M21 11v11M24 11v11M8 13h17M8 20h17"/></g></svg>
        <svg viewBox="0 0 32 32" aria-label="Brennstoffzellenheizung"><circle cx="16" cy="16" r="16" fill="var(--yellow)"/><text x="16" y="11" font-size="6" font-weight="700" fill="#fff" text-anchor="middle" font-family="Open Sans, sans-serif">H2</text><g stroke="#fff" stroke-width="1.4"><path d="M10 14v9M13 14v9M16 14v9M19 14v9M22 14v9M9 16h14M9 21h14"/></g></svg>
        <svg viewBox="0 0 32 32" aria-label="Badsanierung"><circle cx="16" cy="16" r="16" fill="var(--blue-icon)"/><path d="M7 16h18l-2 6H9z" fill="#fff"/><path d="M10 22l-1 2M22 22l1 2" stroke="#fff" stroke-width="1.4"/><circle cx="14" cy="12" r="1.3" fill="#fff"/><circle cx="17" cy="11" r="1" fill="#fff"/></svg>
        <svg viewBox="0 0 32 32" aria-label="Wärmepumpe"><circle cx="16" cy="16" r="16" fill="var(--grey-icon)"/><rect x="10" y="9" width="12" height="14" rx="1" fill="none" stroke="#fff" stroke-width="1.4"/><circle cx="16" cy="17" r="3" fill="none" stroke="#fff" stroke-width="1.4"/></svg>
      </div>

      <div class="photo photo--client" role="img" aria-label="Foto: zufriedene Kundin mit Tablet auf dem Sofa"></div>

      <div class="process">
        <svg class="process__arrows" viewBox="0 0 116 170" fill="none" stroke="var(--ink)" stroke-width="1">
          <path d="M22 30 Q36 12 54 14"/><path d="M49 10l6 4-6 3"/>
          <path d="M104 66 Q110 90 98 110"/><path d="M96 104l1 7 6-3"/>
        </svg>
        <div class="process__step process__step--1"><strong>1. BERATUNG</strong>Wir beraten Sie ausführlich.</div>
        <div class="process__step process__step--2"><strong>2. ANGEBOT</strong>Sie erhalten ein persönliches Angebot.</div>
        <div class="process__step process__step--3"><strong>3. MONTAGE</strong>Wir sind pünktlich, zuverlässig und arbeiten sauber.</div>
      </div>

      <p class="claim">Ihr zuverlässigen Heizungsspezialist und eingetragener<strong>Meisterbetrieb seit 20 Jahren</strong></p>
    </section>

    <section class="panel panel--inside-right">
      <h2 class="staff-title"><strong>Bestens geschultes Fachpersonal</strong>für Ihre Anforderungen</h2>

      <div class="photo photo--boiler-room" role="img" aria-label="Foto: moderner Heizungsraum mit Kesselanlagen und Rohrleitungen"></div>

      <dl class="tasks tasks--main">
        <dt>Wartung</dt>
        <dd>• Zentralheizung Öl &amp; Gas (alle Hersteller)<br>• Solaranlagen<br>• Luft/Wasser Wärmepumpen<br>• jegliche Gasgeräte (Durchlauferhitzer, Einzelofen, Kachelofen, Heizwertthermen etc…)</dd>
        <dt>Störungsbeseitigung &amp; Reparatur</dt>
        <dd>Heizung- und Sanitäranlagen</dd>
        <dt>Testen und aufbereiten</dt>
        <dd>Ihres Heizungswasser</dd>
      </dl>

      <dl class="tasks tasks--more">
        <dd>nach HTR 123 Standard</dd>
        <dt>Spülen von Heizungsanlagen</dt>
        <dd>Fußbodenheizung</dd>
        <dt>Notdienst</dt>
        <dd>Heizung</dd>
        <dt>Spülen &amp; Entlüften</dt>
        <dd>Solaranlagen</dd>
        <dt>Hilfe</dt>
        <dd>Flexible, schnell &amp; unkompliziert</dd>
        <dt>Austausch &amp; Modernisierung</dt>
        <dd>Heizungsanlagen</dd>
      </dl>

      <ul class="benefits">
        <li>HEIZKOSTEN SPAREN</li>
        <li>GENIESSEN &amp; WOHLFÜHLEN</li>
        <li>KLIMASCHUTZ</li>
      </ul>
    </section>
  </main>
</body>
</html>
```